you will use Ai to Copy the website Quellabyx.com to come up with the basic frame work and it will give you the understanding of how I would like Zandoprik.com to be like. Zandoprik.com is a peer to peer rv rental site very similar to both of the other rv rental sites the difference is that are commission based 20% and above per rental and we will be one flat monthly rate and they keep all the earnings. Below is photo that will help you with the color scheme and the look and feel of the design

```html
<!DOCTYPE html>
<html lang="en">
<head>
<meta charset="utf-8">
<title>Zandoprik.com — Peer to peer RV rentals</title>
<link href="https://fonts.googleapis.com/css2?family=Gelasio:wght@400;500&family=Jost:wght@400;500;600;700&display=swap" rel="stylesheet">
<style>
:root{
  --bg:#f3f1ea;
  --ink:#1d2330;
  --muted:#7a7d86;
  --navy:#1b2456;
  --navy-2:#232d66;
  --green:#8fba34;
  --green-dark:#5d8c1f;
  --line:#dcd9cf;
  --white:#ffffff;
  --star:#2f9a3a;
  --bolt:#f2a516;
}
*{box-sizing:border-box;margin:0;padding:0}
html,body{width:1200px;height:4129px;overflow:hidden}
body{background:var(--bg);font-family:'Jost',sans-serif;color:var(--ink);position:relative}
.abs{position:absolute}
.serif{font-family:'Gelasio',serif;font-weight:400}
.btn-green{background:linear-gradient(90deg,var(--green),var(--green-dark));color:var(--white);border-radius:30px;font-size:10px;font-weight:600;letter-spacing:.3px;text-transform:uppercase;display:flex;align-items:center;justify-content:center}
.btn-white{background:var(--white);color:var(--ink);border-radius:30px;font-size:9.5px;font-weight:600;text-transform:uppercase;display:flex;align-items:center;justify-content:center}
.photo{border-radius:12px;overflow:hidden}

/* header */
.brand{left:125px;top:20px;font-family:'Jost',sans-serif;font-weight:700;font-size:26px;color:var(--navy)}
.nav{top:32px;font-size:13px;color:var(--ink)}
.nav.active{text-decoration:underline;text-underline-offset:3px;font-weight:500}
.header-rule{left:125px;top:77px;width:948px;height:1px;background:var(--line)}

/* hero */
.hero-title{left:0;width:1200px;top:112px;text-align:center;font-size:56px;line-height:62px}
.hero-title span{color:var(--green)}
.search{left:125px;top:260px;width:945px;height:63px;background:var(--white);border-radius:40px;box-shadow:0 4px 16px rgba(0,0,0,.05)}
.field{top:16px}
.field small{display:block;font-size:9px;color:var(--muted)}
.field b{display:block;font-size:11px;font-weight:500;margin-top:2px}
.field-sep{top:14px;width:1px;height:36px;background:var(--line)}
.search-go{right:4px;top:5px;width:54px;height:54px;border-radius:50%;background:var(--navy);display:flex;align-items:center;justify-content:center}

.promo{top:396px;height:528px;width:585px}
.promo h3{position:absolute;left:50px;top:385px;font-size:27px;line-height:32px;color:var(--white)}
.promo p{position:absolute;left:50px;top:460px;font-size:10px;line-height:14px;color:var(--white);width:280px}
.promo .btn-white{position:absolute;top:424px;width:128px;height:37px}

/* rentals */
.sec-title{left:0;width:1200px;text-align:center}
.card{top:1113px;width:233px}
.card .img{height:209px;border-radius:12px;position:relative}
.tag{position:absolute;left:18px;top:18px;background:var(--white);border-radius:20px;font-size:8px;font-weight:600;padding:4px 10px}
.fav{position:absolute;right:16px;top:16px;width:20px;height:20px;border-radius:50%;background:var(--white);display:flex;align-items:center;justify-content:center}
.dots3{position:absolute;left:50%;bottom:12px;transform:translateX(-50%);display:flex;gap:4px}
.dots3 i{width:4px;height:4px;border-radius:50%;background:var(--white)}
.card h4{font-family:'Gelasio',serif;font-weight:400;font-size:15px;margin:20px 0 0 18px}
.card .meta{font-size:9px;color:var(--muted);margin:6px 0 0 18px;line-height:15px}
.card .row{display:flex;justify-content:space-between;margin:14px 18px 0 18px;font-size:11.5px;font-weight:600}
.card .row .rate{font-weight:400;font-size:9px;color:var(--muted);display:flex;align-items:center;gap:4px}
.pager{display:flex;gap:5px}
.pager i{width:7px;height:7px;border-radius:50%;background:var(--navy)}
.pager i.on{background:var(--green)}

/* parks */
.parks{left:125px;top:1573px;width:948px;height:523px;background:radial-gradient(ellipse at 70% 40%,var(--navy-2),var(--navy));border-radius:12px}
.parks-photo{left:22px;top:21px;width:387px;height:481px;border-radius:12px;background:linear-gradient(175deg,#c9d4dc 0%,#8c9aa3 30%,#7a5c3e 55%,#4f6a34 80%,#2f4325 100%)}
.parks-photo h4{position:absolute;left:32px;top:348px;color:var(--white);font-size:27px}
.parks-photo p{position:absolute;left:32px;top:382px;color:var(--white);font-family:'Gelasio',serif;font-size:14px}
.avatars{display:flex;align-items:center}
.avatars i{width:36px;height:36px;border-radius:50%;border:2px solid var(--white);margin-right:-8px;background:linear-gradient(135deg,#b9c3a0,#5f6d48)}
.avatars .more{background:var(--white);color:var(--ink);font-style:normal;font-size:8px;font-weight:600;display:flex;align-items:center;justify-content:center;text-align:center;line-height:9px}

/* locations */
.loc{top:2451px;width:306px}
.loc .img{height:372px;border-radius:10px}
.loc h4{font-family:'Gelasio',serif;font-weight:400;font-size:21px;margin-top:24px}
.loc .bar{display:flex;align-items:center;margin-top:16px}
.loc .btn-green{margin-left:28px;width:93px;height:36px}

/* destinations */
.tabs{left:125px;top:3033px;font-size:12px;display:flex;gap:44px}
.tabs .on{font-weight:500;text-decoration:underline;text-underline-offset:4px;color:var(--navy)}
.dest{font-size:10.5px;font-weight:500}
.dest small{display:block;font-size:8.5px;color:var(--muted);font-weight:400;margin-top:2px}

/* app band */
.app{left:10px;top:3404px;width:1179px;height:204px;background:linear-gradient(100deg,#a7c942 0%,#8fb832 45%,#5f8d20 100%);border-radius:12px 12px 0 0}
.app small{position:absolute;left:115px;top:50px;font-family:'Gelasio',serif;font-size:17px;color:var(--white)}
.app h3{position:absolute;left:115px;top:84px;font-size:29px;line-height:36px;color:var(--white)}
.store{position:absolute;top:85px;width:120px;height:36px;background:var(--white);border-radius:20px;display:flex;align-items:center;gap:7px;padding-left:12px}
.store span{font-size:6.5px;color:var(--muted);display:block;text-transform:uppercase}
.store b{font-size:11px;font-weight:600;display:block;color:var(--ink)}
.store i{width:14px;height:14px;border-radius:50%;background:var(--ink);display:block}

/* footer */
.footer{left:10px;top:3608px;width:1179px;height:509px;background:var(--navy);border-radius:0 0 12px 12px;color:var(--white)}
.f-brand{position:absolute;left:160px;top:75px;font-weight:700;font-size:40px;color:var(--white)}
.contact{position:absolute;top:88px;display:flex;align-items:center;gap:14px}
.contact .ico{width:46px;height:46px;background:rgba(255,255,255,.1);border-radius:6px;display:flex;align-items:center;justify-content:center}
.contact small{display:block;font-size:9px;opacity:.7}
.contact b{display:block;font-size:19px;font-weight:500}
.f-rule{position:absolute;left:166px;top:200px;width:849px;height:1px;background:rgba(255,255,255,.18)}
.col{position:absolute;top:258px}
.col h5{font-size:14px;font-weight:600;margin-bottom:12px}
.col li{list-style:none;font-size:9px;line-height:20px;opacity:.85}
.social{position:absolute;top:324px;width:30px;height:30px;border-radius:50%;background:rgba(255,255,255,.12)}
.legal{position:absolute;left:165px;top:372px;font-size:8.5px;line-height:16px;opacity:.85}
.totop{position:absolute;left:1101px;top:404px;width:40px;height:40px;border-radius:50%;background:linear-gradient(135deg,var(--green),var(--green-dark));display:flex;align-items:center;justify-content:center}
</style>
</head>
<body>

<!-- header -->
<div class="abs brand">Zandoprik.com</div>
<div class="abs nav active" style="left:517px">RV Rentals</div>
<div class="abs nav" style="left:602px">Campgrounds</div>
<div class="abs btn-green" style="left:878px;top:24px;width:119px;height:35px;font-size:9px">Become a host</div>
<svg class="abs" style="left:1013px;top:33px" width="17" height="14" viewBox="0 0 17 14"><path d="M0 1h17M0 7h17M0 13h17" stroke="#1d2330" stroke-width="1.6"/></svg>
<div class="abs" style="left:1043px;top:27px;width:29px;height:29px;border-radius:50%;background:var(--white);display:flex;align-items:center;justify-content:center"><svg width="11" height="11" viewBox="0 0 12 12"><circle cx="6" cy="3.5" r="2.8" fill="#1d2330"/><path d="M1 12c0-3 2.2-5 5-5s5 2 5 5z" fill="#1d2330"/></svg></div>
<div class="abs header-rule"></div>

<!-- hero -->
<h1 class="abs hero-title serif">Start your adventure<br><span>with a camper van|</span></h1>
<div class="abs search">
  <div class="abs field" style="left:32px"><small>Select</small><b>Location</b></div>
  <div class="abs field-sep" style="left:250px"></div>
  <div class="abs field" style="left:271px"><small>Dates</small><b>Any Dates</b></div>
  <div class="abs field-sep" style="left:395px"></div>
  <div class="abs field" style="left:415px"><small>Guests</small><b>2 Guests</b></div>
  <div class="abs field-sep" style="left:530px"></div>
  <div class="abs field" style="left:549px"><small>Driver's ages</small><b>25+</b></div>
  <div class="abs field-sep" style="left:678px"></div>
  <div class="abs field" style="left:697px"><small>Rental type</small><b>All types</b></div>
  <div class="abs search-go"><svg width="16" height="16" viewBox="0 0 16 16"><circle cx="6.5" cy="6.5" r="5" stroke="#fff" stroke-width="1.6" fill="none"/><path d="M10.5 10.5L15 15" stroke="#fff" stroke-width="1.6"/></svg></div>
</div>

<div class="abs promo photo" style="left:10px" role="img" aria-label="White camper van with open side door parked by a mountain lake at dusk">
  <div style="position:absolute;inset:0;background:linear-gradient(180deg,#9fb3b5 0%,#4f7478 35%,#3b5046 60%,#2a2a22 100%)"></div>
  <h3 class="serif">Your adventure<br>starts here.</h3>
  <p>Rent the perfect RV for your next adventure — or list your RV and keep more of what you earn.</p>
  <div class="btn-white" style="left:402px">Get it delivered</div>
</div>
<div class="abs promo photo" style="left:604px" role="img" aria-label="Camper van with awning set up at a desert campsite at sunset">
  <div style="position:absolute;inset:0;background:linear-gradient(180deg,#6e7f8c 0%,#a88b6a 40%,#6b4a30 70%,#2b211a 100%)"></div>
  <h3 class="serif">Less set up. More<br>quality time.</h3>
  <p>Rent the perfect RV for your next adventure — or list your RV and keep more of what you earn.</p>
  <div class="btn-white" style="left:400px">Pick it up</div>
</div>

<!-- rentals -->
<h2 class="abs sec-title serif" style="top:1018px;font-size:32px">Find the best RV rentals in the country</h2>
<p class="abs sec-title" style="top:1066px;font-size:11px;color:var(--muted)">Explore the open road in the perfect RV rental. Or, get one delivered and set up for you.</p>

<div class="abs card" style="left:115px">
  <div class="img" role="img" aria-label="Class C motorhome parked under a dramatic sky" style="background:linear-gradient(180deg,#7d8a99,#c7ccd2 55%,#4c4f55)"><span class="tag">Highly rated</span><span class="fav"><svg width="9" height="9" viewBox="0 0 10 10"><path d="M5 9L1 5a2.2 2.2 0 013.9-2.6L5 2.6l.1-.2A2.2 2.2 0 019 5z" fill="#8fba34"/></svg></span><span class="dots3"><i></i><i></i><i></i></span></div>
  <h4>Vanish Standard</h4>
  <div class="meta">Camper van • Sleeps 2 • 20 ft<br>Jersey City, NJ</div>
  <div class="row"><span><span style="color:var(--bolt)">⚡</span> $359 / day</span><span class="rate"><span style="color:var(--star)">★</span>5.0 (28)</span></div>
</div>
<div class="abs card" style="left:360px">
  <div class="img" role="img" aria-label="Motorhome parked in a sunlit forest" style="background:linear-gradient(180deg,#b7c26a,#5d7a2e 55%,#2d3a1d)"><span class="tag">Highly rated</span><span class="fav"><svg width="9" height="9" viewBox="0 0 10 10"><path d="M5 9L1 5a2.2 2.2 0 013.9-2.6L5 2.6l.1-.2A2.2 2.2 0 019 5z" fill="#8fba34"/></svg></span><span class="dots3"><i></i><i></i><i></i></span></div>
  <h4>2001 Veltmar Roamvan</h4>
  <div class="meta">Camper van • Sleeps 2 • 17 ft<br>Los Angeles, CA</div>
  <div class="row"><span><span style="color:var(--bolt)">⚡</span> $342 / night</span><span class="rate"><span style="color:var(--star)">★</span>5.0 (16)</span></div>
</div>
<div class="abs card" style="left:606px">
  <div class="img" role="img" aria-label="Travel trailer on a desert road at golden hour" style="background:linear-gradient(180deg,#e0b27a,#b87a4a 50%,#5a3a26)"><span class="tag">Highly rated</span><span class="fav"><svg width="9" height="9" viewBox="0 0 10 10"><path d="M5 9L1 5a2.2 2.2 0 013.9-2.6L5 2.6l.1-.2A2.2 2.2 0 019 5z" fill="#8fba34"/></svg></span><span class="dots3"><i></i><i></i><i></i></span></div>
  <h4>Goin' Big Triple Slide</h4>
  <div class="meta">Travel trailer • Sleeps 10 • 36 ft<br>Sisters, OR</div>
  <div class="row"><span><span style="color:var(--bolt)">⚡</span> $150 / day</span><span class="rate"><span style="color:var(--star)">★</span>5.0 (12)</span></div>
</div>
<div class="abs card" style="left:851px">
  <div class="img" role="img" aria-label="Dark camper van with glowing interior beside a mountain lake" style="background:linear-gradient(180deg,#a9b4bc,#6c7d86 45%,#3a3f36)"><span class="tag">Highly rated</span><span class="fav"><svg width="9" height="9" viewBox="0 0 10 10"><path d="M5 9L1 5a2.2 2.2 0 013.9-2.6L5 2.6l.1-.2A2.2 2.2 0 019 5z" fill="#8fba34"/></svg></span><span class="dots3"><i></i><i></i><i></i></span></div>
  <h4>2001 Veltmar Roamvan</h4>
  <div class="meta">Camper van • Sleeps 2 • 17 ft<br>Los Angeles, CA</div>
  <div class="row"><span><span style="color:var(--bolt)">⚡</span> $200 / night</span><span class="rate"><span style="color:var(--star)">★</span>5.0 (22)</span></div>
</div>
<div class="abs pager" style="left:582px;top:1494px"><i></i><i class="on"></i><i></i></div>

<!-- national parks -->
<div class="abs parks">
  <div class="abs parks-photo" role="img" aria-label="Waterfall cascading down a granite cliff in a national park">
    <h4 class="serif">Grand Canyon</h4>
    <p>Arizona</p>
    <div class="avatars" style="position:absolute;left:32px;top:407px"><i></i><i></i><i></i><i class="more">+68</i></div>
    <div class="btn-white" style="position:absolute;left:259px;top:413px;width:96px;height:37px">Book now</div>
  </div>
  <h3 class="abs serif" style="left:480px;top:163px;font-size:32px;line-height:37px;color:var(--white)">Explore rentals near<br>National Parks</h3>
  <p class="abs" style="left:480px;top:238px;font-size:10.5px;color:var(--white)">Cruise to epic locations in the comfort of an RV rental.</p>
  <p class="abs" style="left:480px;top:265px;font-size:25px;font-weight:600;color:var(--white)">From $45/night</p>
  <div class="abs btn-green" style="left:481px;top:324px;width:128px;height:37px">View all parks</div>
  <div class="abs pager" style="left:482px;top:436px"><i style="background:#fff"></i><i class="on"></i><i style="background:#fff"></i></div>
  <div class="abs" role="img" aria-label="Class A motorhome with green striped livery" style="left:601px;top:385px;width:277px;height:160px;border-radius:40px 20px 14px 14px;background:linear-gradient(180deg,#f2f0e8 0%,#d9d6cb 55%,#6f9a2c 75%,#2b2f33 100%)"></div>
</div>

<!-- locations -->
<h2 class="abs sec-title serif" style="top:2210px;font-size:42px;line-height:44px">Select Your Location &amp; Find Trusted<br>Services In Your Area</h2>
<p class="abs sec-title serif" style="top:2316px;font-size:15px">Camper Vans • Motorhomes • Travel Trailers • Fifth Wheels • Toy Haulers</p>
<div class="abs btn-green" style="left:535px;top:2360px;width:128px;height:37px">Explore RVs</div>

<div class="abs loc" style="left:125px">
  <div class="img" role="img" aria-label="Granite dome reflected in a lake with autumn trees" style="background:linear-gradient(180deg,#9fb2c2,#8a8b7a 40%,#c98a2e 62%,#3d4a3c)"></div>
  <h4>Yosemite, CA</h4>
  <div class="bar"><div class="avatars"><i></i><i></i><i></i><i class="more">VIEW<br>ALL</i></div><div class="btn-green">Book now</div></div>
</div>
<div class="abs loc" style="left:447px">
  <div class="img" role="img" aria-label="Aerial view of an RV park clearing among pine forest" style="background:linear-gradient(180deg,#a9b9c6,#4e6a3a 30%,#c8b69a 65%,#4d5f35)"></div>
  <h4>Bayfield, Co</h4>
  <div class="bar"><div class="avatars"><i></i><i></i><i></i><i class="more">VIEW<br>ALL</i></div><div class="btn-green">Book now</div></div>
</div>
<div class="abs loc" style="left:769px">
  <div class="img" role="img" aria-label="Aerial view of a ranch house among oak trees in dry hill country" style="background:linear-gradient(180deg,#b89f7c,#8c7252 45%,#5b6036 75%,#6e5a3e)"></div>
  <h4>Hill Country, TX</h4>
  <div class="bar"><div class="avatars"><i></i><i></i><i></i><i class="more">VIEW<br>ALL</i></div><div class="btn-green">Book now</div></div>
</div>

<!-- destinations -->
<div class="abs tabs"><span class="on">Popular RV Rental Destinations</span><span>Search RVs by State</span></div>

<div class="abs dest" style="left:125px;top:3094px">Atlanta, GA<small>751 RV rentals</small></div>
<div class="abs dest" style="left:261px;top:3094px">Austin, TX<small>783 RV rentals</small></div>
<div class="abs dest" style="left:408px;top:3094px">Boston, MA<small>351 RV rentals</small></div>
<div class="abs dest" style="left:572px;top:3094px">Chicago, IL<small>455 RV rentals</small></div>
<div class="abs dest" style="left:718px;top:3094px">Columbus, OH<small>410 RV rentals</small></div>
<div class="abs dest" style="left:876px;top:3094px">Maui, HI<small>149 RV rentals</small></div>
<div class="abs dest" style="left:1011px;top:3094px">Raleigh, NC<small>259 RV rentals</small></div>

<div class="abs dest" style="left:125px;top:3153px">Houston, TX<small>567 RV rentals</small></div>
<div class="abs dest" style="left:261px;top:3153px">Kailua-Kona, HI<small>148 RV rentals</small></div>
<div class="abs dest" style="left:408px;top:3153px">Kauai, HI<small>82 RV rentals</small></div>
<div class="abs dest" style="left:572px;top:3153px">Las Vegas, NV<small>436 RV rentals</small></div>
<div class="abs dest" style="left:718px;top:3153px">Los Angeles, CA<small>2,834 RV rentals</small></div>
<div class="abs dest" style="left:876px;top:3153px">Portland, OR<small>645 RV rentals</small></div>
<div class="abs dest" style="left:1011px;top:3153px">Honolulu, HI<small>312 RV rentals</small></div>

<div class="abs dest" style="left:125px;top:3212px">Nashville, TN<small>311 RV rentals</small></div>
<div class="abs dest" style="left:261px;top:3212px">New York, NY<small>575 RV rentals</small></div>
<div class="abs dest" style="left:408px;top:3212px">Oklahoma City, OK<small>139 RV rentals</small></div>
<div class="abs dest" style="left:572px;top:3212px">Orlando, FL<small>1,326 RV rentals</small></div>
<div class="abs dest" style="left:718px;top:3212px">Phoenix, AZ<small>953 RV rentals</small></div>
<div class="abs dest" style="left:876px;top:3212px">Denver, CO<small>1,278 RV rentals</small></div>
<div class="abs dest" style="left:1011px;top:3212px">Minneapolis, MN<small>432 RV rentals</small></div>

<div class="abs dest" style="left:125px;top:3272px">San Antonio, TX<small>690 RV rentals</small></div>
<div class="abs dest" style="left:261px;top:3272px">San Diego, CA<small>2,093 RV rentals</small></div>
<div class="abs dest" style="left:408px;top:3272px">San Francisco, CA<small>1,447 RV rentals</small></div>
<div class="abs dest" style="left:572px;top:3272px">Seattle, WA<small>790 RV rentals</small></div>
<div class="abs dest" style="left:718px;top:3272px">Dallas, TX<small>715 RV rentals</small></div>
<div class="abs dest" style="left:876px;top:3272px">Miami, FL<small>483 RV rentals</small></div>
<div class="abs dest" style="left:1011px;top:3272px">Salt Lake City, UT<small>857 RV rentals</small></div>

<!-- app band -->
<div class="abs app">
  <small>Download Zandoprik app</small>
  <h3 class="serif">RV rentals made simple. More freedom for<br>travelers. More earnings for RV owners.</h3>
  <div class="store" style="left:815px"><i></i><div><span>Get it on</span><b>App Market</b></div></div>
  <div class="store" style="left:945px"><i></i><div><span>Download on the</span><b>Play Shelf</b></div></div>
</div>

<!-- footer -->
<footer class="abs footer">
  <div class="f-brand">Zandoprik.com</div>
  <div class="contact" style="left:551px">
    <div class="ico"><svg width="16" height="16" viewBox="0 0 16 16"><path d="M3 1l3 .5 1 3.5-2 1.2a9 9 0 004.8 4.8L11 9l3.5 1 .5 3-2 2C7 15 1 9 1 3z" fill="#fff"/></svg></div>
    <div><small>Call us Now</small><b>555-013-2468</b></div>
  </div>
  <div class="contact" style="left:791px">
    <div class="ico"><svg width="16" height="12" viewBox="0 0 16 12"><rect width="16" height="12" rx="1.5" fill="#fff"/><path d="M1 1l7 6 7-6" stroke="#1b2456" stroke-width="1.4" fill="none"/></svg></div>
    <div><small>Write to us</small><b>info@zandoprik.com</b></div>
  </div>
  <div class="f-rule"></div>

  <div class="abs" style="left:171px;top:260px;display:flex;align-items:center;gap:8px;font-size:11px;font-weight:600;text-decoration:underline"><span style="width:13px;height:13px;border-radius:50%;background:var(--green);display:block"></span>Language &amp; currency</div>
  <span class="social" style="left:167px"></span>
  <span class="social" style="left:210px"></span>
  <span class="social" style="left:252px"></span>
  <span class="social" style="left:294px"></span>
  <div class="legal">Terms &nbsp;|&nbsp; Privacy &nbsp;|&nbsp; Your Privacy Choices &nbsp;|&nbsp; Sitemap<br>© 2026 Zandoprik, Inc. All rights reserved.</div>

  <div class="col" style="left:458px"><h5>Quick Links</h5><ul><li>Where it all began</li><li>Careers</li><li>Stories and news</li><li>Travel journal</li><li>About</li></ul></div>
  <div class="col" style="left:615px"><h5>Guest Travel</h5><ul><li>Group bookings</li><li>Gift cards</li><li>Delivery</li><li>National park guides</li><li>One-way rentals</li><li>Road trip guides</li><li>RV parks &amp; campgrounds</li><li>Guide to all RV types</li></ul></div>
  <div class="col" style="left:786px"><h5>Hosting</h5><ul><li>Become an RV host</li><li>Rigboard demo</li><li>Affiliate program</li><li>RV insurance</li><li>Host iOS app</li><li>Host Android app</li></ul></div>
  <div class="col" style="left:937px"><h5>Support</h5><ul><li>How it works</li><li>Help center</li><li>Contact us</li><li>Give us feedback</li><li>LLM info</li></ul></div>

  <div class="totop"><svg width="12" height="8" viewBox="0 0 12 8"><path d="M1 7l5-5 5 5" stroke="#fff" stroke-width="1.6" fill="none"/></svg></div>
</footer>

</body>
</html>
```